Google Form Graphic to suit our Brand and industry

Create a graphic / image for us to put at the top of our client enquiry google form.
The image will be a section of an architectural home with our branding over the top. Preferably translucent.
The image must suit the shape of the google forms image, which is an elongated rectangle
#003d5d - brand colour

Target Market(s)

residential home owners, high end architectural homes

Industry/Entity Type

Residential construction

Colors
0054AA
0677BA
7BADD7
CADEEF
E8F1F8

Requirements
Must have
• our branding and a photo of an architectural home in the background

```html
<!DOCTYPE html>
<html lang="en">
<head>
<meta charset="utf-8">
<title>New Client Enquiry Form</title>
<link rel="stylesheet" href="https://fonts.googleapis.com/css2?family=Montserrat:wght@600&family=Roboto:wght@400;500;700&family=Roboto+Condensed:wght@400&display=swap">
<style>
  :root {
    --page-grey: #e5e5e5;
    --form-cream: #f6efdf;
    --card-white: #ffffff;
    --card-border: #dcdad3;
    --brand-navy: #0b4560;
    --accent-blue: #4f7df2;
    --tab-gold: #e1b35b;
    --text-dark: #202124;
    --text-muted: #5f6368;
    --required-red: #d93025;
    --dotted-line: #9aa0a6;
  }
  * { box-sizing: border-box; margin: 0; padding: 0; }
  html, body { width: 937px; height: 1200px; overflow: hidden; }
  body {
    background: var(--page-grey);
    font-family: "Roboto", Arial, sans-serif;
    color: var(--text-dark);
    position: relative;
  }
  .form-column {
    position: absolute; left: 97px; top: 0; width: 751px; height: 1200px;
    background: var(--form-cream);
  }
  .header-banner {
    position: absolute; left: 127px; top: 15px; width: 701px; height: 255px;
    overflow: hidden;
  }
  .header-photo {
    position: absolute; inset: 0;
    background:
      linear-gradient(180deg, rgba(60,90,110,0.25) 0%, rgba(20,60,85,0.1) 40%, rgba(40,150,180,0.35) 65%, rgba(60,80,90,0.4) 100%),
      linear-gradient(90deg, #3e5a4c 0%, #4d6a74 25%, #5f7e92 45%, #6f8fa6 60%, #4d7060 85%, #3b5a47 100%);
  }
  .header-tint { position: absolute; inset: 0; background: rgba(0,61,93,0.35); }
  .brand-name {
    position: absolute; left: 0; right: 0; top: 100px; text-align: center;
    font-family: "Montserrat", Arial, sans-serif; font-weight: 600;
    font-size: 36px; letter-spacing: 1px; color: #ffffff;
  }
  .brand-tagline {
    position: absolute; left: 0; right: 0; top: 150px; text-align: center;
    font-family: "Roboto Condensed", Arial, sans-serif; font-size: 25px; color: #ffffff;
  }
  .section-tab {
    position: absolute; left: 127px; top: 284px; width: 137px; height: 42px;
    background: var(--brand-navy); color: #fff; border-radius: 6px 6px 0 0;
    font-size: 17px; line-height: 42px; text-align: center;
  }
  .section-bar {
    position: absolute; left: 127px; top: 325px; width: 701px; height: 11px;
    background: var(--brand-navy);
  }
  .card {
    position: absolute; left: 127px; width: 701px; background: var(--card-white);
    border: 1px solid var(--card-border); border-radius: 8px;
  }
  .title-card { top: 334px; height: 196px; border-top: none; border-radius: 0 0 8px 8px; }
  .form-title {
    position: absolute; left: 23px; top: 64px; width: 579px; padding-bottom: 6px;
    font-size: 28px; font-weight: 400; border-bottom: 1px solid #5f6368;
  }
  .title-actions { position: absolute; left: 617px; top: 68px; }
  .format-toolbar {
    position: absolute; left: 34px; top: 117px; display: flex; gap: 22px; align-items: center;
    color: var(--text-muted); font-size: 15px; font-weight: 500;
  }
  .tool-bold { font-weight: 700; }
  .tool-italic { font-style: italic; }
  .tool-underline { text-decoration: underline; }
  .form-description {
    position: absolute; left: 23px; top: 156px; font-size: 12px; color: var(--text-dark);
  }
  .question-card { height: 125px; }
  .question-card.active { border-left: 6px solid var(--accent-blue); }
  .question-label { position: absolute; left: 23px; top: 26px; font-size: 15px; }
  .question-card.active .question-label { left: 24px; }
  .required { color: var(--required-red); margin-left: 6px; }
  .answer-placeholder {
    position: absolute; left: 23px; top: 64px; width: 328px; padding-bottom: 4px;
    font-size: 12px; color: var(--text-muted); border-bottom: 1px dotted var(--dotted-line);
  }
  .question-card.active .answer-placeholder { left: 18px; }
  .section-nav {
    position: absolute; left: 127px; top: 1099px; font-size: 13px; color: var(--text-dark);
    display: flex; align-items: center;
  }
  .section-nav .nav-choice { margin-left: 16px; width: 300px; }
  .next-tab {
    position: absolute; left: 127px; top: 1169px; width: 111px; height: 40px;
    background: var(--tab-gold); border-radius: 6px 6px 0 0;
    font-size: 13px; line-height: 34px; text-align: center; color: var(--text-dark);
  }
  .side-toolbar {
    position: absolute; left: 838px; top: 1099px; width: 14px; height: 110px;
    background: var(--card-white); border: 1px solid var(--card-border); border-radius: 6px 0 0 0;
  }
</style>
</head>
<body>
  <div class="form-column"></div>

  <header class="header-banner">
    <div class="header-photo" role="img" aria-label="Photo of an architectural home with a pool, timber screen wall and tropical garden"></div>
    <div class="header-tint"></div>
    <div class="brand-name">Marlo Build</div>
    <div class="brand-tagline">Architectural Homes, Crafted Together</div>
  </header>

  <div class="section-tab">Section 1 of 4</div>
  <div class="section-bar"></div>

  <section class="card title-card">
    <h1 class="form-title">New Client Enquiry Form</h1>
    <div class="title-actions">
      <svg width="70" height="26" viewBox="0 0 70 26" aria-hidden="true">
        <path d="M6 4l5 5 5-5M6 22l5-5 5 5" fill="none" stroke="#5f6368" stroke-width="1.8"/>
        <circle cx="58" cy="6" r="2" fill="#5f6368"/><circle cx="58" cy="12" r="2" fill="#5f6368"/><circle cx="58" cy="18" r="2" fill="#5f6368"/>
      </svg>
    </div>
    <div class="format-toolbar">
      <span class="tool-bold">B</span>
      <span class="tool-italic">I</span>
      <span class="tool-underline">U</span>
      <svg width="18" height="12" viewBox="0 0 18 12" aria-hidden="true"><rect x="1" y="2" width="8" height="8" rx="4" fill="none" stroke="#5f6368" stroke-width="1.6"/><rect x="9" y="2" width="8" height="8" rx="4" fill="none" stroke="#5f6368" stroke-width="1.6"/></svg>
      <svg width="16" height="14" viewBox="0 0 16 14" aria-hidden="true"><path d="M2 2h12M8 2L5 12M9 9l5 4M14 9l-5 4" fill="none" stroke="#5f6368" stroke-width="1.6"/></svg>
    </div>
    <p class="form-description">We would love to hear your thoughts or feedback on how we can improve your experience!</p>
  </section>

  <section class="card question-card active" style="top:544px">
    <div class="question-label">Firstly, how did you hear about us?<span class="required">*</span></div>
    <div class="answer-placeholder">Short answer text</div>
  </section>

  <section class="card question-card" style="top:682px">
    <div class="question-label">Name</div>
    <div class="answer-placeholder">Short answer text</div>
  </section>

  <section class="card question-card" style="top:819px">
    <div class="question-label">Phone</div>
    <div class="answer-placeholder">Short answer text</div>
  </section>

  <section class="card question-card" style="top:956px">
    <div class="question-label">Email</div>
    <div class="answer-placeholder">Short answer text</div>
  </section>

  <div class="section-nav">
    <span>After section 1</span>
    <span class="nav-choice">Continue to next section</span>
    <svg width="10" height="6" viewBox="0 0 10 6" aria-hidden="true"><path d="M0 0h10L5 6z" fill="#5f6368"/></svg>
  </div>

  <div class="side-toolbar"></div>

  <div class="next-tab">Section 2 of 4</div>
</body>
</html>
```